BOLD ORCHID Personal Training Website.

I am looking for a website design for Word Press URL I already have. I have it as 10 very simple pages. Once home page design is set we can use that look on all other pages. I have uploaded a word document that has an outline of what I am looking for. Please take the time to review this. I want to add this is for a WordPress site.

Target Market(s)

Women 25-55

Industry/Entity Type

Health And Wellness

Coding

Coded - Design and coding required

Number of Pages Required

5+ page

```html
<!DOCTYPE html>
<html lang="en">
<head>
<meta charset="utf-8">
<title>BOLD ORCHID – Personal Training</title>
<link rel="stylesheet" href="https://fonts.googleapis.com/css2?family=Montserrat:wght@400;500;600;700;800&family=Open+Sans:wght@400;600&family=Kaushan+Script&display=swap">
<style>
:root{
  --red:#e3202a;
  --teal:#1ba79c;
  --ink:#222429;
  --text:#6b6e73;
  --light:#eef1f3;
  --white:#ffffff;
  --dark:#1e1f22;
  --head:"Montserrat",sans-serif;
  --body:"Open Sans",sans-serif;
}
*{box-sizing:border-box;margin:0;padding:0}
html,body{width:1200px;height:3965px;overflow:hidden;background:var(--white)}
body{position:relative;font-family:var(--body);color:var(--text)}
.abs{position:absolute}
section,header,footer{position:absolute;left:0;width:1200px}
.title{font-family:var(--head);font-weight:700;color:var(--ink);font-size:32px;text-align:center;width:100%}
.sub{font-size:13px;text-align:center;width:100%;color:var(--text)}
.btn-outline{position:absolute;height:38px;border:2px solid var(--red);border-radius:20px;font-family:var(--head);font-weight:600;font-size:12px;color:var(--ink);display:flex;align-items:center;justify-content:center;background:var(--white)}
.arrow{position:absolute;width:20px;height:20px}
.photo{position:absolute}

/* hero */
.hero{top:0;height:568px;background:radial-gradient(ellipse at 40% 30%,#7a7a7a 0%,#3f3f3f 45%,#1b1b1b 100%)}
.nav{position:absolute;top:0;left:0;width:1200px;height:116px}
.brand{position:absolute;left:74px;top:22px;display:flex;align-items:center;gap:10px}
.brand-dot{width:58px;height:58px;border-radius:50%;background:var(--red)}
.brand-name{font-family:var(--head);font-weight:700;font-size:17px;color:var(--white);letter-spacing:.5px;white-space:nowrap}
.menu{position:absolute;left:312px;top:52px;display:flex;gap:20px;font-family:var(--head);font-size:11px;font-weight:500;color:var(--white);white-space:nowrap}
.menu .active{color:var(--teal)}
.signup{position:absolute;left:1016px;top:40px;width:114px;height:36px;border-radius:18px;background:var(--red);color:var(--white);font-family:var(--head);font-weight:600;font-size:13px;display:flex;align-items:center;justify-content:center}
.follow{position:absolute;left:60px;top:262px;display:flex;flex-direction:column;align-items:center;gap:10px}
.follow i{display:block;width:13px;height:13px;border:1.5px solid var(--white);border-radius:3px}
.follow span{writing-mode:vertical-rl;transform:rotate(180deg);font-family:var(--head);font-size:11px;color:var(--white);margin-top:6px}
.quote{position:absolute;top:222px;width:100%;text-align:center;color:var(--white)}
.quote .q1{font-family:var(--head);font-weight:700;font-size:44px}
.quote .q2{font-family:"Kaushan Script",cursive;font-size:34px;margin-top:2px}
.hero-btn{position:absolute;left:503px;top:345px;width:194px;height:38px;border:2px solid var(--white);border-radius:20px;color:var(--white);font-family:var(--head);font-weight:600;font-size:12px;display:flex;align-items:center;justify-content:center}
.hero-btn em{font-style:normal;color:var(--teal);margin-left:4px}
.hero-dots{position:absolute;left:1117px;top:262px;display:flex;flex-direction:column;gap:14px}
.hero-dots i{width:10px;height:10px;border:1.5px solid var(--white);border-radius:50%;display:block}
.hero-dots i.on{background:var(--white)}

/* about */
.about{top:568px;height:450px;overflow:hidden}
.about h2{position:absolute;left:206px;top:62px;font-family:var(--head);font-weight:700;font-size:30px;color:var(--ink)}
.about h3{position:absolute;left:206px;top:116px;font-family:var(--head);font-weight:600;font-size:15px;color:var(--teal)}
.about p{position:absolute;left:206px;width:500px;font-size:11.5px;line-height:1.55}

/* certifications */
.certs{top:1018px;height:528px;background:var(--light)}
.cert{position:absolute;top:150px;width:250px;height:193px;background:var(--white);border:1px solid #dfe3e6}
.cert .seal{position:absolute;left:18px;bottom:22px;width:48px;height:22px;background:#c8d6e2;border-radius:3px}
.cert .line{position:absolute;left:30px;height:4px;background:#e3e6e9;border-radius:2px}
.cert-label{position:absolute;top:356px;width:250px;text-align:center;font-family:var(--head);font-weight:600;font-size:14px;color:var(--ink);line-height:1.35}
.expand{position:absolute;left:106px;top:76px;width:38px;height:38px;border-radius:50%;background:var(--teal)}

/* videos */
.videos{top:1546px;height:542px}
.caption{position:absolute;left:272px;top:444px;width:360px;font-family:var(--head);font-weight:600;font-size:14px;color:var(--ink);line-height:1.45}
.btn-red{position:absolute;border-radius:20px;background:var(--red);color:var(--white);font-family:var(--head);font-weight:600;font-size:12px;display:flex;align-items:center;justify-content:center}

/* blog */
.blog{top:2088px;height:428px}
.blog-intro{position:absolute;left:0;top:0;width:410px;height:428px;background:var(--teal);color:var(--white)}
.blog-intro h2{position:absolute;left:71px;top:132px;font-family:var(--head);font-weight:700;font-size:30px}
.blog-intro p{position:absolute;left:71px;top:185px;width:230px;font-size:12px;line-height:1.55}
.blog-intro .view{position:absolute;left:71px;top:264px;width:126px;height:36px;border:2px solid var(--white);border-radius:18px;font-family:var(--head);font-weight:600;font-size:11px;display:flex;align-items:center;justify-content:center}
.post{position:absolute;width:395px;height:214px;padding:30px 26px}
.post h4{font-family:var(--head);font-weight:700;font-size:14px;color:var(--ink);line-height:1.4}
.post p{font-size:11.5px;line-height:1.6;margin-top:12px}
.post .more{margin-top:14px;font-family:var(--head);font-weight:600;font-size:11px;color:var(--red);display:flex;align-items:center;gap:8px}
.post .more i{width:10px;height:10px;border:1.5px solid var(--teal);border-radius:50%;display:block}

/* training */
.training{top:2516px;height:440px;background:linear-gradient(160deg,#f3f5f7 0%,#f3f5f7 40%,var(--white) 40%)}
.program{position:absolute;top:153px;width:250px;height:178px;border-radius:6px;overflow:hidden}
.program .num{position:absolute;left:18px;top:112px;font-family:var(--head);font-weight:700;font-size:26px;color:var(--white)}
.program .name{position:absolute;left:18px;top:146px;font-family:var(--head);font-weight:600;font-size:14px;color:var(--white)}

/* testimonials */
.testimonials{top:2979px;left:71px;width:1058px;height:378px;background:radial-gradient(ellipse at 50% 40%,#6a6a6a 0%,#3c3c3c 60%,#2a2a2a 100%)}
.testimonials h2{position:absolute;top:68px;width:100%;text-align:center;font-family:var(--head);font-weight:700;font-size:30px;color:var(--white)}
.testimonials .mark{position:absolute;top:112px;width:100%;text-align:center;font-family:var(--head);font-weight:800;font-size:30px;color:var(--red);line-height:1}
.testimonials p{position:absolute;left:216px;top:160px;width:626px;text-align:center;font-size:13px;line-height:1.6;color:var(--white)}
.testimonials .who{position:absolute;top:280px;width:100%;text-align:center;font-family:var(--head);font-weight:600;font-size:15px;color:var(--teal)}
.testimonials .where{position:absolute;top:304px;width:100%;text-align:center;font-size:11px;color:var(--white)}
.t-dots{position:absolute;left:897px;top:176px;display:flex;flex-direction:column;gap:10px}
.t-dots i{width:9px;height:9px;border:1.5px solid var(--white);border-radius:50%;display:block}
.t-dots i.on{background:var(--white)}

/* contact */
.contact{top:3400px;height:385px}
.field{position:absolute;height:36px;border-bottom:1px solid #dcdfe2;font-family:var(--head);font-size:10px;font-weight:500;color:var(--ink);letter-spacing:.5px}

/* footer */
.footer{top:3785px;height:180px;background:var(--dark)}
.social{position:absolute;top:58px;width:36px;height:36px;border-radius:50%;border:2px solid var(--red)}
.copy{position:absolute;top:112px;width:100%;text-align:center;font-size:11px;color:#b9bbbe}
.copy b{color:var(--red);font-weight:600}
</style>
</head>
<body>

<header class="hero">
  <div class="photo" role="img" aria-label="Close-up of a black kettlebell and dumbbell in a dim gym, black and white" style="inset:0;background:radial-gradient(circle at 45% 45%,#8a8a8a 0%,#4a4a4a 40%,#1a1a1a 90%)"></div>
  <div class="photo" style="inset:0;background:rgba(0,0,0,.28)"></div>
  <nav class="nav">
    <div class="brand"><span class="brand-dot"></span><span class="brand-name">BOLD ORCHID</span></div>
    <div class="menu">
      <span class="active">Home</span><span>Certifications</span><span>Bio</span><span>Blog</span><span>Videos</span><span>Online Training</span><span>Nutrition</span><span>Merchandize</span><span>Contact Us</span>
    </div>
    <div class="signup">Sign Up</div>
  </nav>
  <div class="follow"><i></i><i></i><span>Follow Us</span></div>
  <div class="quote">
    <div class="q1">“If it doesn’t Challenge you,</div>
    <div class="q2">it won’t Change you”</div>
  </div>
  <div class="hero-btn">Sign Up For <em>Free Online</em></div>
  <div class="hero-dots"><i></i><i class="on"></i><i></i><i></i><i></i></div>
  <svg class="abs" style="left:591px;top:516px" width="18" height="12" viewBox="0 0 18 12"><path d="M2 2l7 7 7-7" fill="none" stroke="#fff" stroke-width="2"/></svg>
</header>

<section class="about">
  <svg class="abs" style="left:0;top:0" width="1200" height="450" viewBox="0 0 1200 450"><polygon points="990,0 1200,0 1200,170 1050,450 800,450" fill="var(--teal)"/></svg>
  <h2>About Us</h2>
  <h3>There are many variations of passages Ipsum available.</h3>
  <p style="top:142px">Contrary to popular belief, Lorem Ipsum is not simply random text. It has roots in a piece of classical Latin literature from 45 BC, making it over 2000 years old. Daniel Whitmore, a Latin professor at Harrowgate College in Vermont, looked up one of the more obscure Latin words, consectetur, from a Lorem ...</p>
  <p style="top:228px">There are many variations of passages of Lorem Ipsum available, but the majority have suffered alteration in some form, by injected humour, or randomised words which don't look even slightly believable ...</p>
  <div class="btn-outline" style="left:206px;top:338px;width:126px">Discover More</div>
  <div class="photo" role="img" aria-label="Woman in a visor and sports top running in a race" style="left:745px;top:72px;width:384px;height:304px;background:linear-gradient(135deg,#8fa6b0 0%,#5e6e6a 45%,#b06a72 75%,#3d4448 100%)"></div>
</section>

<section class="certs">
  <div class="title abs" style="top:62px">KSTA certification</div>
  <div class="sub abs" style="top:100px">There are many variations of passages of Lorem Ipsum available</div>
  <svg class="arrow" style="left:150px;top:238px" viewBox="0 0 20 20"><path d="M13 3l-7 7 7 7" fill="none" stroke="#555" stroke-width="1.6"/></svg>
  <svg class="arrow" style="left:1030px;top:238px" viewBox="0 0 20 20"><path d="M7 3l7 7-7 7" fill="none" stroke="#555" stroke-width="1.6"/></svg>

  <div class="cert" style="left:212px">
    <span class="line" style="top:26px;width:190px"></span><span class="line" style="top:44px;width:120px;left:65px"></span><span class="line" style="top:70px;width:150px;left:50px"></span><span class="line" style="top:90px;width:190px"></span><span class="line" style="top:104px;width:190px"></span><span class="seal"></span><span class="line" style="top:160px;width:70px;left:150px"></span>
  </div>
  <div class="cert" style="left:475px">
    <span class="line" style="top:26px;width:190px"></span><span class="line" style="top:44px;width:120px;left:65px"></span><span class="line" style="top:130px;width:190px"></span><span class="seal"></span><span class="line" style="top:160px;width:70px;left:150px"></span>
    <span class="expand"></span>
    <svg class="abs" style="left:116px;top:86px" width="18" height="18" viewBox="0 0 18 18"><path d="M2 7V2h5M16 11v5h-5M2 2l5 5M16 16l-5-5" fill="none" stroke="#fff" stroke-width="1.6"/></svg>
  </div>
  <div class="cert" style="left:738px">
    <span class="line" style="top:26px;width:190px"></span><span class="line" style="top:44px;width:120px;left:65px"></span><span class="line" style="top:70px;width:150px;left:50px"></span><span class="line" style="top:90px;width:190px"></span><span class="line" style="top:104px;width:190px"></span><span class="seal"></span><span class="line" style="top:160px;width:70px;left:150px"></span>
  </div>
  <div class="cert-label" style="left:212px">Corrective Exercise<br>Specialist</div>
  <div class="cert-label" style="left:475px">Fitness Nutrition Specialist<br>(FNS)</div>
  <div class="cert-label" style="left:738px">Certified Personal<br>Trainer</div>
  <div class="btn-outline" style="left:538px;top:420px;width:124px">View All</div>
</section>

<section class="videos">
  <div class="title abs" style="top:60px">Videos</div>
  <div class="sub abs" style="top:98px">There are many variations of passages of Lorem</div>
  <svg class="arrow" style="left:218px;top:272px" viewBox="0 0 20 20"><path d="M13 3l-7 7 7 7" fill="none" stroke="#555" stroke-width="1.6"/></svg>
  <svg class="arrow" style="left:962px;top:272px" viewBox="0 0 20 20"><path d="M7 3l7 7-7 7" fill="none" stroke="#555" stroke-width="1.6"/></svg>
  <div class="photo" role="img" aria-label="Loaded barbell with weight plate on a gym floor, black and white" style="left:272px;top:140px;width:653px;height:283px;border-radius:4px;background:radial-gradient(circle at 45% 50%,#5a5a5a 0%,#2d2d2d 35%,#9a9a9a 70%,#6b6b6b 100%)"></div>
  <svg class="abs" style="left:573px;top:256px" width="52" height="52" viewBox="0 0 52 52"><circle cx="26" cy="26" r="24" fill="none" stroke="#fff" stroke-width="3"/><path d="M21 16l14 10-14 10z" fill="#fff"/></svg>
  <div class="caption">But I must explain to you how all this mistaken idea of denouncing pleasure</div>
  <div class="btn-red" style="left:801px;top:444px;width:124px;height:38px">View All</div>
</section>

<section class="blog">
  <div class="blog-intro">
    <h2>Latest Blog</h2>
    <p>At vero eos et accusamus et iusto odio dignissimos ducimus qui blanditiis praesentium voluptatum.</p>
    <div class="view">View All Blog</div>
  </div>
  <div class="photo" role="img" aria-label="Woman lifting dumbbells in a bright gym" style="left:410px;top:0;width:396px;height:214px;background:linear-gradient(120deg,#3a4452 0%,#8c7468 45%,#c9a98e 70%,#4d4a48 100%)"></div>
  <div class="post" style="left:806px;top:0;background:var(--white)">
    <h4>Contrary to popular belief, Lorem Ipsum is not simply random text.</h4>
    <p>There are many variations of passages of Lorem Ipsum available, but the majority have suffered alteration in some form, by injected humour, or randomised ...</p>
  </div>
  <div class="post" style="left:410px;top:214px;background:var(--light)">
    <h4>Contrary to popular belief, Lorem Ipsum is not simply random text.</h4>
    <p>There are many variations of passages of Lorem Ipsum available, but the majority have suffered alteration in some form, by injected humour, or randomised ...</p>
    <div class="more"><i></i>Explore More</div>
  </div>
  <div class="photo" role="img" aria-label="Barbell plates resting on a gym floor, black and white" style="left:806px;top:214px;width:394px;height:214px;background:radial-gradient(circle at 40% 55%,#3a3a3a 0%,#6a6a6a 45%,#c4c4c4 100%)"></div>
</section>

<section class="training">
  <div class="title abs" style="top:68px">Online Training</div>
  <div class="sub abs" style="top:106px">But I must explain to you how all this mistaken idea of denouncing</div>
  <svg class="arrow" style="left:150px;top:232px" viewBox="0 0 20 20"><path d="M13 3l-7 7 7 7" fill="none" stroke="#555" stroke-width="1.6"/></svg>
  <svg class="arrow" style="left:1030px;top:232px" viewBox="0 0 20 20"><path d="M7 3l7 7-7 7" fill="none" stroke="#555" stroke-width="1.6"/></svg>
  <div class="program" style="left:206px">
    <div class="photo" role="img" aria-label="Group of women training with resistance bands" style="inset:0;background:linear-gradient(135deg,#7d6f6c 0%,#a8878a 40%,#3e3a3c 100%)"></div>
    <div class="photo" style="inset:0;background:linear-gradient(180deg,rgba(0,0,0,0) 40%,rgba(0,0,0,.6) 100%)"></div>
    <span class="num">01</span><span class="name">Weight Loss</span>
  </div>
  <div class="program" style="left:475px">
    <div class="photo" role="img" aria-label="Muscular athlete in a dark gym" style="inset:0;background:radial-gradient(circle at 55% 40%,#6b6b6b 0%,#2b2b2b 55%,#151515 100%)"></div>
    <span class="num">02</span><span class="name" style="color:var(--teal)">Body Building</span>
  </div>
  <div class="program" style="left:744px">
    <div class="photo" role="img" aria-label="Gym interior with weight racks" style="inset:0;background:linear-gradient(135deg,#5a4a48 0%,#2d2a2a 45%,#6b5f5a 100%)"></div>
    <div class="photo" style="inset:0;background:linear-gradient(180deg,rgba(0,0,0,0) 40%,rgba(0,0,0,.6) 100%)"></div>
    <span class="num">03</span><span class="name">Stretching</span>
  </div>
  <div class="btn-outline" style="left:534px;top:360px;width:132px">View All Training</div>
</section>

<section class="testimonials" role="img" aria-label="Blurred gym background behind testimonial">
  <h2>Testimonials</h2>
  <span class="mark">“ ”</span>
  <p>I wasn’t sure if Marissa was interested in training my then 11-year-old daughter, but after talking with her she was 100% committed to what we wanted to accomplish with our daughter. After their first intro session together, my daughter was excited and nervous about this new journey of training ...</p>
  <div class="t-dots"><i></i><i class="on"></i><i></i></div>
  <div class="who">Rosalie</div>
  <div class="where">Cedar Bluff CO</div>
</section>

<section class="contact">
  <div class="title abs" style="top:22px">Contact Us</div>
  <div class="sub abs" style="top:62px">We are Here to help you 24 hours a day.</div>
  <div class="field" style="left:283px;top:102px;width:300px">NAME:</div>
  <div class="field" style="left:618px;top:102px;width:312px">EMAIL:</div>
  <div class="field" style="left:283px;top:160px;width:300px">PHONE:</div>
  <div class="field" style="left:618px;top:160px;width:312px">ADDRESS:</div>
  <div class="field" style="left:283px;top:214px;width:647px;height:48px">COMMENTS:</div>
  <div class="btn-outline" style="left:552px;top:282px;width:96px">Send</div>
</section>

<footer class="footer">
  <span class="social" style="left:560px"></span>
  <span class="social" style="left:604px;background:var(--red)"></span>
  <div class="copy">© 2018 <b>BOLD ORCHID</b>. All Right Reserved.</div>
</footer>

</body>
</html>
```